A Label for an ECO Friendly Spirit Company

Design a label which can be used for vodka and gin (London Dry Gin). It should be Square type Like the Shape File you see in the uploads. VORK means Local Eco friendly Authentic and Fair. We want a cool and slim label that calls for eco-friendly. We want to use it for our premium
Vodka and our London Dry Gin. Please use the logo and design it in Square Type.

40%vol, 700ml

Target Market(s)

spirits and events

Industry/Entity Type

SPIRITS

Colors
00AB8E
00BBA5
67D7C9
C6EFE9
E9F9F6
59FF00
82FF00
B8FF75
E3FFCB
F4FFEA

Requirements
Must have
• Logo from VORK, Squaee Shape

```html
<!DOCTYPE html>
<html lang="en">
<head>
<meta charset="utf-8">
<title>VORK London Dry Gin Label</title>
<link rel="stylesheet" href="https://fonts.googleapis.com/css2?family=Cinzel:wght@600;700&family=Montserrat:wght@500;600;700&display=swap">
<style>
  :root {
    --teal: #3bb18b;
    --paper: #f6f6f6;
    --white: #ffffff;
    --page: #ffffff;
  }
  html, body {
    margin: 0;
    padding: 0;
    width: 1200px;
    height: 1084px;
    overflow: hidden;
    background: var(--page);
  }
  .label {
    display: block;
    width: 1200px;
    height: 1084px;
  }
  .label-body { filter: drop-shadow(0 10px 22px rgba(0,0,0,0.28)); }
  .fill-teal { fill: var(--teal); }
  .fill-paper { fill: var(--paper); }
  .frame-line { fill: none; stroke: var(--white); stroke-width: 3; }
  .frame-line--top { stroke: var(--teal); }
  .brand-name {
    font-family: "Montserrat", sans-serif;
    font-weight: 600;
    font-size: 66px;
    letter-spacing: 2px;
    fill: var(--teal);
  }
  .title-serif {
    font-family: "Cinzel", serif;
    font-weight: 700;
    fill: var(--white);
  }
  .title-origin { font-size: 50px; letter-spacing: 7px; }
  .title-product { font-size: 92px; letter-spacing: 3px; }
  .values {
    font-family: "Montserrat", sans-serif;
    font-weight: 500;
    fill: var(--white);
  }
  .values-line1 { font-size: 22px; letter-spacing: 0.5px; }
  .values-line2 { font-size: 18px; letter-spacing: 9px; }
  .spec {
    font-family: "Montserrat", sans-serif;
    font-weight: 700;
    font-size: 27px;
    font-variant: small-caps;
    fill: var(--white);
  }
</style>
</head>
<body>
<svg class="label" viewBox="0 0 1200 1084" xmlns="http://www.w3.org/2000/svg" role="img" aria-label="VORK London Dry Gin diamond label">
  <defs>
    <clipPath id="top-zone"><rect x="0" y="0" width="1200" height="485"/></clipPath>
  </defs>

  <g class="label-body">
    <polygon class="fill-teal" points="604,199 954,549 604,899 254,549"/>
  </g>
  <polygon class="fill-paper" clip-path="url(#top-zone)" points="604,203 950,549 604,895 258,549"/>

  <g class="frame">
    <polygon class="frame-line" points="604,216 937,549 604,882 271,549"/>
    <polygon class="frame-line" points="604,231 922,549 604,867 286,549"/>
    <g clip-path="url(#top-zone)">
      <polygon class="frame-line frame-line--top" points="604,216 937,549 604,882 271,549"/>
      <polygon class="frame-line frame-line--top" points="604,231 922,549 604,867 286,549"/>
    </g>
  </g>

  <g class="brand">
    <text class="brand-name" x="604" y="420" text-anchor="middle">VORK</text>
  </g>

  <g class="title">
    <text class="title-serif title-origin" x="614" y="538" text-anchor="middle">London</text>
    <text class="title-serif title-product" x="603" y="610" text-anchor="middle">Dry Gin</text>
  </g>

  <g class="values-block">
    <text class="values values-line1" x="603" y="658" text-anchor="middle">LOCAL ECO-FRIENDLY</text>
    <text class="values values-line2" x="610" y="681" text-anchor="middle">AUTHENTIC FAIR</text>
  </g>

  <g class="specs">
    <text class="spec" x="603" y="746" text-anchor="middle">40%vol</text>
    <text class="spec" x="603" y="777" text-anchor="middle">700ml</text>
  </g>
</svg>
</body>
</html>
```